The Lantern Assembly Pitchdeck Template

The Lantern Assembly would like a branded pitch deck template design for members to use when presenting their projects and proposals. The deck should include 10-15 different slide designs, each with the same branded theme, but with a variety of icon graphics and other design features that will empower members to easily create a beautiful pitch deck just by adding written content.

Please visit thelantern.org to get a sense for our branding - purple, space, galaxy, white font and the planetary logo are some commonalities.

Here are 2 google drive links with some additional designs

https://files.cloudnestbox.net/share/u/1/dir/8KpqZr3Tn5Yb-wLxVd2Hc-Qm4jEsAf7Ug

https://files.cloudnestbox.net/share/u/1/dir/6Rtb2-Lm9Xc4-hNwq813Fvkzpe_Jd7Sa

```html
<!DOCTYPE html>
<html lang="en">
<head>
<meta charset="utf-8">
<title>The Lantern Assembly Pitch Deck Template</title>
<link rel="stylesheet" href="https://fonts.googleapis.com/css2?family=Montserrat:wght@400;500;600;700;800&display=swap">
<style>
:root{
  --purple:#7a4db3;
  --purple-light:#a57bd6;
  --purple-deep:#4e2a86;
  --navy:#24398a;
  --navy-deep:#182a6b;
  --ink:#3a3550;
  --muted:#8a86a0;
  --page:#e8e6ee;
  --stage:#efedf3;
  --white:#ffffff;
}
*{box-sizing:border-box;margin:0;padding:0}
html,body{width:1200px;height:3424px;overflow:hidden}
body{font-family:"Montserrat",Arial,sans-serif;color:var(--ink);background:var(--page);position:relative}

.hero{position:absolute;left:0;top:0;width:1200px;height:730px;background:var(--stage)}
.brand-mark{position:absolute;display:flex;align-items:center;gap:8px;font-weight:700;color:var(--white);font-size:13px}
.brand-mark .dot{width:14px;height:14px;border-radius:50%;background:var(--white)}
.hero .brand-mark{right:40px;top:40px;color:var(--purple-deep);font-size:16px}
.hero .brand-mark .dot{background:var(--purple-deep);width:18px;height:18px}

.slide{position:absolute;width:552px;height:310px;overflow:hidden;background:var(--white)}
.slide.hero-slide{left:160px;top:110px;width:880px;height:495px;box-shadow:0 20px 50px rgba(40,20,80,.25)}
.bg-purple{background:linear-gradient(135deg,#6a3fa3 0%,#9b6fd0 55%,#7d55b8 100%)}
.bg-blue{background:linear-gradient(135deg,var(--navy-deep) 0%,var(--navy) 45%,#6f4db0 100%)}

.title-block{position:absolute;left:28px;top:100px;color:var(--white)}
.title-block .kicker{font-weight:800;font-size:26px;letter-spacing:.5px}
.title-block .headline{font-weight:500;font-size:26px;margin-top:2px}
.title-block .sub{font-size:10px;margin-top:6px;opacity:.9}
.pill{display:inline-block;margin-top:14px;padding:5px 12px;border-radius:12px;background:rgba(255,255,255,.2);font-size:8px;color:var(--white)}
.hero-slide .title-block{left:44px;top:170px}
.hero-slide .kicker{font-size:42px}
.hero-slide .headline{font-size:42px}
.hero-slide .sub{font-size:16px}
.hero-slide .pill{font-size:12px;padding:7px 18px;border-radius:16px}
.slide .brand-mark{left:26px;top:24px}
.hero-slide .brand-mark{left:44px;top:40px;font-size:18px}
.footer-bar{position:absolute;left:0;bottom:0;width:100%;height:18px;background:var(--purple-deep);color:var(--white);font-size:7px;display:flex;align-items:center;justify-content:center}
.hero-slide .footer-bar{height:28px;font-size:11px}
.strip{position:absolute;left:0;bottom:0;width:100%;height:8px;background:linear-gradient(90deg,var(--navy),var(--purple))}

.heading{position:absolute;left:0;top:22px;width:100%;text-align:center;color:var(--purple);font-weight:600;font-size:17px;letter-spacing:.5px}
.para{font-size:7px;line-height:1.45;color:var(--muted)}
.item-title{font-size:9px;font-weight:700;color:var(--purple)}
.item-title span{font-weight:400;color:var(--ink)}

.toc-grid{position:absolute;left:70px;top:70px;width:420px;display:grid;grid-template-columns:1fr 1fr;gap:22px 40px}
.toc-item{display:flex;gap:8px}
.toc-num{width:18px;height:18px;flex:none;border-radius:4px;background:var(--purple);color:var(--white);font-size:8px;font-weight:700;display:flex;align-items:center;justify-content:center}

.who-text{position:absolute;left:30px;top:40px;width:240px}
.who-text h2{color:var(--purple);font-weight:600;font-size:20px;text-align:center;margin-bottom:12px}
.who-text .para{margin-bottom:8px}
.photo{position:absolute}
.photo-night{right:0;top:0;width:262px;height:310px;background:linear-gradient(180deg,#3b2e6e,#6d5aa8 60%,#241b45)}

.icon-grid{position:absolute;left:40px;top:66px;width:472px;display:grid;grid-template-columns:1fr 30px 1fr 30px;gap:12px 12px;align-items:center}
.icon-circle{width:26px;height:26px;border-radius:50%;background:var(--navy);display:flex;align-items:center;justify-content:center}
.icon-circle.alt{background:var(--purple)}

.envision .heading{color:var(--white);top:18px;font-size:18px}
.vision-row{position:absolute;left:34px;top:58px;width:484px;display:flex;gap:18px}
.vision-card{flex:1;text-align:center;color:var(--white)}
.vision-card .photo{position:static;height:110px;border-radius:2px}
.vision-card .label{margin-top:8px;font-size:9px;font-weight:700;letter-spacing:.5px}
.vision-card .para{color:rgba(255,255,255,.85);margin-top:4px}
.ph-a{background:linear-gradient(135deg,#f0b37a,#c26a8d)}
.ph-b{background:linear-gradient(135deg,#2f6fb8,#6fb0d8)}
.ph-c{background:linear-gradient(135deg,#e08a5a,#6b3f8e)}

.timeline{position:absolute;left:20px;top:56px}
.timeline text{font-family:"Montserrat",Arial,sans-serif}

.pyramid{position:absolute;left:30px;top:70px}
.pyr-list{position:absolute;left:300px;top:66px;width:220px;display:flex;flex-direction:column;gap:14px}
.pyr-item{display:flex;gap:8px}
.pyr-item .sq{width:10px;height:10px;flex:none;margin-top:2px}

.chart{position:absolute;left:22px;top:46px}
.chart-legend{position:absolute;left:360px;top:80px;width:170px;display:flex;flex-direction:column;gap:20px}
.legend-item{display:flex;gap:8px}
.legend-item .sq{width:12px;height:12px;flex:none;border-radius:2px}

.partners-title{position:absolute;left:30px;top:140px;color:var(--white);font-weight:700;font-size:26px;letter-spacing:1px}

.project-text{position:absolute;left:30px;top:50px;width:200px}
.project-text h2{color:var(--purple);font-weight:600;font-size:18px;line-height:1.1;margin-bottom:6px}
.project-text .lead{font-size:8px;color:var(--ink);margin-bottom:8px}
.photo-galaxy{right:0;top:0;width:300px;height:310px;background:linear-gradient(135deg,#2a1f5e,#6a3fa3 50%,#1c1642)}

.photo-partner{left:0;top:0;width:260px;height:310px;background:linear-gradient(135deg,#1b2a4f,#3c4f86 50%,#12182f)}
.partner-text{position:absolute;left:260px;top:0;width:292px;height:310px;background:var(--navy-deep);color:var(--white);padding:80px 40px 0}
.partner-text h2{font-weight:600;font-size:18px;letter-spacing:1px;margin-bottom:10px}
.partner-text .para{color:rgba(255,255,255,.8)}

.quote-row{position:absolute;left:26px;top:40px;width:500px;display:flex;gap:16px}
.quote-card{flex:1;height:230px;padding:16px 14px;color:var(--white)}
.quote-card:nth-child(odd){background:var(--navy)}
.quote-card:nth-child(even){background:var(--purple)}
.quote-mark{font-size:30px;font-weight:800;line-height:1}
.quote-card .para{color:rgba(255,255,255,.85);margin-top:6px}
.quote-card .who{font-size:8px;font-weight:700;margin-top:14px}

.contact{position:absolute;left:30px;top:130px;color:var(--white)}
.contact h2{font-size:14px;font-weight:700;margin-bottom:8px}
.contact-line{display:flex;align-items:center;gap:6px;font-size:7.5px;margin-bottom:5px}
.contact-line svg{flex:none}
</style>
</head>
<body>

<section class="hero">
  <div class="brand-mark"><span class="dot"></span>The Lantern Assembly</div>
  <div class="slide hero-slide bg-purple">
    <div class="brand-mark"><span class="dot"></span>The Lantern Assembly</div>
    <div class="title-block">
      <div class="kicker">PRESENTATION</div>
      <div class="headline">Title Goes Here!</div>
      <div class="sub">Subtitle of Presentation Goes Here</div>
      <div class="pill">Presenter Name | Date</div>
    </div>
    <div class="footer-bar">© The Lantern Assembly</div>
  </div>
</section>

<!-- Row 1 -->
<div class="slide bg-purple" style="left:40px;top:752px">
  <div class="brand-mark"><span class="dot"></span>The Lantern Assembly</div>
  <div class="title-block">
    <div class="kicker">PRESENTATION</div>
    <div class="headline">Title Goes Here!</div>
    <div class="sub">Subtitle of Presentation Goes Here</div>
    <div class="pill">Presenter Name | Date</div>
  </div>
</div>
<div class="slide bg-blue" style="left:608px;top:752px">
  <div class="brand-mark"><span class="dot"></span>The Lantern Assembly</div>
  <div class="title-block">
    <div class="kicker">PRESENTATION</div>
    <div class="headline">Title Goes Here!</div>
    <div class="sub">Subtitle of Presentation Goes Here</div>
    <div class="pill">Presenter Name | Date</div>
  </div>
</div>

<!-- Row 2 -->
<div class="slide bg-purple" style="left:40px;top:1086px">
  <div class="brand-mark"><span class="dot"></span>The Lantern Assembly</div>
  <div class="title-block">
    <div class="kicker">PRESENTATION</div>
    <div class="headline">Title Goes Here!</div>
    <div class="sub">Subtitle of Presentation Goes Here</div>
    <div class="pill">Presenter Name | Date</div>
  </div>
  <div class="footer-bar">© The Lantern Assembly</div>
</div>
<div class="slide" style="left:608px;top:1086px">
  <div class="heading">TABLE OF CONTENTS</div>
  <div class="toc-grid">
    <div class="toc-item"><div class="toc-num">01</div><div><div class="item-title">Title <span>Goes Here!</span></div><p class="para">Add a short line about this part of the talk.</p></div></div>
    <div class="toc-item"><div class="toc-num">04</div><div><div class="item-title">Title <span>Goes Here!</span></div><p class="para">Add a short line about this part of the talk.</p></div></div>
    <div class="toc-item"><div class="toc-num">02</div><div><div class="item-title">Title <span>Goes Here!</span></div><p class="para">Add a short line about this part of the talk.</p></div></div>
    <div class="toc-item"><div class="toc-num">05</div><div><div class="item-title">Title <span>Goes Here!</span></div><p class="para">Add a short line about this part of the talk.</p></div></div>
    <div class="toc-item"><div class="toc-num">03</div><div><div class="item-title">Title <span>Goes Here!</span></div><p class="para">Add a short line about this part of the talk.</p></div></div>
    <div class="toc-item"><div class="toc-num">06</div><div><div class="item-title">Title <span>Goes Here!</span></div><p class="para">Add a short line about this part of the talk.</p></div></div>
  </div>
  <div class="strip"></div>
</div>

<!-- Row 3 -->
<div class="slide" style="left:40px;top:1420px">
  <div class="who-text">
    <h2>WHO ARE WE</h2>
    <p class="para">We are a community of members who share ideas, gather around bold projects and help each other bring proposals to life with care and purpose.</p>
    <p class="para">Use this space to tell your story, your mission and the values that guide the work you do together every day.</p>
    <p class="para">Add a closing line that invites the audience to learn more.</p>
  </div>
  <div class="photo photo-night" role="img" aria-label="Photo of a person seated under a purple night sky"></div>
</div>
<div class="slide" style="left:608px;top:1420px">
  <div class="heading">SLIDE TITLE GOES HERE</div>
  <div class="icon-grid">
    <div><div class="item-title">Title <span>Goes Here</span></div><p class="para">Short supporting text for this point.</p></div>
    <div class="icon-circle"><svg width="12" height="12" viewBox="0 0 12 12"><circle cx="6" cy="6" r="4" fill="none" stroke="#fff" stroke-width="1.5"/></svg></div>
    <div><div class="item-title">Title <span>Goes Here</span></div><p class="para">Short supporting text for this point.</p></div>
    <div class="icon-circle alt"><svg width="12" height="12" viewBox="0 0 12 12"><path d="M2 6l3 3 5-6" fill="none" stroke="#fff" stroke-width="1.5"/></svg></div>
    <div><div class="item-title">Title <span>Goes Here</span></div><p class="para">Short supporting text for this point.</p></div>
    <div class="icon-circle alt"><svg width="12" height="12" viewBox="0 0 12 12"><rect x="2" y="3" width="8" height="6" fill="none" stroke="#fff" stroke-width="1.5"/></svg></div>
    <div><div class="item-title">Title <span>Goes Here</span></div><p class="para">Short supporting text for this point.</p></div>
    <div class="icon-circle"><svg width="12" height="12" viewBox="0 0 12 12"><path d="M6 1l1.5 3.5L11 5 8.2 7.3 9 11 6 9 3 11l.8-3.7L1 5l3.5-.5z" fill="#fff"/></svg></div>
    <div><div class="item-title">Title <span>Goes Here</span></div><p class="para">Short supporting text for this point.</p></div>
    <div class="icon-circle"><svg width="12" height="12" viewBox="0 0 12 12"><path d="M2 10V6M6 10V3M10 10V5" stroke="#fff" stroke-width="1.5"/></svg></div>
    <div><div class="item-title">Title <span>Goes Here</span></div><p class="para">Short supporting text for this point.</p></div>
    <div class="icon-circle alt"><svg width="12" height="12" viewBox="0 0 12 12"><path d="M6 1a3.5 3.5 0 0 0-3.5 3.5C2.5 7.5 6 11 6 11s3.5-3.5 3.5-6.5A3.5 3.5 0 0 0 6 1z" fill="#fff"/></svg></div>
  </div>
  <div class="strip"></div>
</div>

<!-- Row 4 -->
<div class="slide bg-blue envision" style="left:40px;top:1754px">
  <div class="heading">WHAT WE ENVISION</div>
  <div class="vision-row">
    <div class="vision-card"><div class="photo ph-a" role="img" aria-label="Photo of a community gathering at sunset"></div><div class="label">PEOPLE</div><p class="para">A short line about this vision.</p></div>
    <div class="vision-card"><div class="photo ph-b" role="img" aria-label="Photo of the Earth seen from space"></div><div class="label">PLANET</div><p class="para">A short line about this vision.</p></div>
    <div class="vision-card"><div class="photo ph-c" role="img" aria-label="Photo of raised hands against a warm sky"></div><div class="label">PURPOSE</div><p class="para">A short line about this vision.</p></div>
  </div>
</div>
<div class="slide" style="left:608px;top:1754px">
  <div class="heading">SLIDE TITLE GOES HERE!</div>
  <svg class="timeline" width="512" height="220" viewBox="0 0 512 220">
    <path d="M40 60 H420 a40 40 0 0 1 0 80 H40" fill="none" stroke="#cfc4e6" stroke-width="2"/>
    <g font-size="8" font-weight="700" fill="#7a4db3" text-anchor="middle">
      <circle cx="90" cy="60" r="14" fill="#24398a"/><text x="90" y="34">2018</text>
      <circle cx="250" cy="60" r="14" fill="#7a4db3"/><text x="250" y="34">2019</text>
      <circle cx="410" cy="60" r="14" fill="#24398a"/><text x="410" y="34">2020</text>
      <circle cx="410" cy="140" r="14" fill="#7a4db3"/><text x="410" y="172">2021</text>
      <circle cx="250" cy="140" r="14" fill="#24398a"/><text x="250" y="172">2022</text>
      <circle cx="90" cy="140" r="14" fill="#7a4db3"/><text x="90" y="172">2023</text>
    </g>
    <g font-size="7" fill="#8a86a0" text-anchor="middle">
      <text x="90" y="96">Title Goes Here</text><text x="250" y="96">Title Goes Here</text><text x="410" y="96">Title Goes Here</text>
      <text x="90" y="186">Title Goes Here</text><text x="250" y="186">Title Goes Here</text><text x="410" y="186">Title Goes Here</text>
    </g>
  </svg>
  <div class="strip"></div>
</div>

<!-- Row 5 -->
<div class="slide" style="left:40px;top:2088px">
  <div class="heading">SLIDE TITLE GOES HERE</div>
  <svg class="pyramid" width="240" height="190" viewBox="0 0 240 190">
    <polygon points="120,0 150,45 90,45" fill="#a57bd6"/>
    <polygon points="88,49 152,49 182,94 58,94" fill="#7a4db3"/>
    <polygon points="56,98 184,98 214,143 26,143" fill="#4e2a86"/>
    <polygon points="24,147 216,147 240,185 0,185" fill="#24398a"/>
  </svg>
  <div class="pyr-list">
    <div class="pyr-item"><span class="sq" style="background:#a57bd6"></span><div><div class="item-title">Title <span>Goes Here</span></div><p class="para">Short supporting text for this level.</p></div></div>
    <div class="pyr-item"><span class="sq" style="background:#7a4db3"></span><div><div class="item-title">Title <span>Goes Here</span></div><p class="para">Short supporting text for this level.</p></div></div>
    <div class="pyr-item"><span class="sq" style="background:#4e2a86"></span><div><div class="item-title">Title <span>Goes Here</span></div><p class="para">Short supporting text for this level.</p></div></div>
    <div class="pyr-item"><span class="sq" style="background:#24398a"></span><div><div class="item-title">Title <span>Goes Here</span></div><p class="para">Short supporting text for this level.</p></div></div>
  </div>
  <div class="strip"></div>
</div>
<div class="slide" style="left:608px;top:2088px">
  <div class="heading">SLIDE TITLE GOES HERE</div>
  <svg class="chart" width="320" height="230" viewBox="0 0 320 230">
    <g stroke="#e6e2ef" stroke-width="1"><line x1="20" y1="40" x2="310" y2="40"/><line x1="20" y1="90" x2="310" y2="90"/><line x1="20" y1="140" x2="310" y2="140"/><line x1="20" y1="190" x2="310" y2="190"/></g>
    <g fill="#7a4db3"><rect x="40" y="100" width="10" height="90"/><rect x="100" y="60" width="10" height="130"/><rect x="160" y="120" width="10" height="70"/><rect x="220" y="50" width="10" height="140"/><rect x="280" y="80" width="10" height="110"/></g>
    <g fill="#24398a"><rect x="53" y="130" width="10" height="60"/><rect x="113" y="110" width="10" height="80"/><rect x="173" y="70" width="10" height="120"/><rect x="233" y="120" width="10" height="70"/><rect x="293" y="100" width="10" height="90"/></g>
    <g font-size="7" fill="#8a86a0" text-anchor="middle" font-family="Montserrat, Arial, sans-serif"><text x="52" y="204">Item 1</text><text x="112" y="204">Item 2</text><text x="172" y="204">Item 3</text><text x="232" y="204">Item 4</text><text x="292" y="204">Item 5</text></g>
  </svg>
  <div class="chart-legend">
    <div class="legend-item"><span class="sq" style="background:#7a4db3"></span><div><div class="item-title">Title <span>Goes Here</span></div><p class="para">Short note on this data series.</p></div></div>
    <div class="legend-item"><span class="sq" style="background:#24398a"></span><div><div class="item-title">Title <span>Goes Here</span></div><p class="para">Short note on this data series.</p></div></div>
    <div class="legend-item"><span class="sq" style="background:#a57bd6"></span><div><div class="item-title">Title <span>Goes Here</span></div><p class="para">Short note on this data series.</p></div></div>
  </div>
  <div class="strip"></div>
</div>

<!-- Row 6 -->
<div class="slide bg-purple" style="left:40px;top:2422px">
  <div class="brand-mark" style="top:100px;left:30px"><span class="dot"></span>The Lantern Assembly</div>
  <div class="partners-title">PARTNERS</div>
</div>
<div class="slide" style="left:608px;top:2422px">
  <div class="project-text">
    <h2>OPEN<br>HORIZON</h2>
    <p class="lead">A Group of Shared Explorations</p>
    <p class="para">Describe the partner project here in a few short lines, what it offers and how members can take part in its work.</p>
  </div>
  <div class="photo photo-galaxy" role="img" aria-label="Image of a glowing purple galaxy with the partner project artwork"></div>
  <div class="strip"></div>
</div>

<!-- Row 7 -->
<div class="slide" style="left:40px;top:2756px">
  <div class="photo photo-partner" role="img" aria-label="Partner artwork on a dark blue starry background"></div>
  <div class="partner-text">
    <h2>MERIDIAN</h2>
    <p class="para">Describe this partner in a few short lines, what they do and how the work connects with your members and mission.</p>
  </div>
</div>
<div class="slide" style="left:608px;top:2756px">
  <div class="quote-row">
    <div class="quote-card"><div class="quote-mark">“</div><p class="para">Add a short quote from a member or partner about the impact of this work.</p><div class="who">Member Name</div></div>
    <div class="quote-card"><div class="quote-mark">“</div><p class="para">Add a short quote from a member or partner about the impact of this work.</p><div class="who">Member Name</div></div>
    <div class="quote-card"><div class="quote-mark">“</div><p class="para">Add a short quote from a member or partner about the impact of this work.</p><div class="who">Member Name</div></div>
  </div>
  <div class="strip"></div>
</div>

<!-- Row 8 -->
<div class="slide bg-purple" style="left:324px;top:3090px">
  <div class="brand-mark" style="top:96px;left:30px"><span class="dot"></span>The Lantern Assembly</div>
  <div class="contact">
    <h2>Contact Us</h2>
    <div class="contact-line"><svg width="9" height="9" viewBox="0 0 10 10"><path d="M2 1h2l1 2.5-1.3 1a6 6 0 0 0 2.8 2.8l1-1.3L10 7v2a1 1 0 0 1-1 1A8 8 0 0 1 1 2a1 1 0 0 1 1-1z" fill="#fff"/></svg>+1 000 000 0000</div>
    <div class="contact-line"><svg width="9" height="9" viewBox="0 0 10 10"><rect x="1" y="2" width="8" height="6" fill="none" stroke="#fff"/><path d="M1 2l4 3 4-3" fill="none" stroke="#fff"/></svg>hello@thelantern.org</div>
    <div class="contact-line"><svg width="9" height="9" viewBox="0 0 10 10"><circle cx="5" cy="5" r="4" fill="none" stroke="#fff"/><path d="M1 5h8M5 1v8" stroke="#fff"/></svg>thelantern.org</div>
    <div class="contact-line"><svg width="9" height="9" viewBox="0 0 10 10"><path d="M5 1a3 3 0 0 0-3 3c0 2.5 3 5 3 5s3-2.5 3-5a3 3 0 0 0-3-3z" fill="#fff"/></svg>Your Address Here</div>
  </div>
  <div class="footer-bar">© The Lantern Assembly</div>
</div>

</body>
</html>
```